Create Website for new Home services company

We need a website built for a new home services company we are primarily a surface refinishing company that repairs cracks in tubs and resurfaces tubs, sinks or vanities also repainting cabinets as well.

```html
<!DOCTYPE html>
<html lang="en">
<head>
<meta charset="utf-8">
<title>Evenglaze Refinishing</title>
<link rel="stylesheet" href="https://fonts.googleapis.com/css2?family=Oswald:wght@400;500;600&family=Open+Sans:wght@400;600&display=swap">
<style>
:root{
  --red:#ec1c24;
  --ink:#111111;
  --dark:#2b2826;
  --grey:#d9d9d9;
  --white:#ffffff;
  --text:#1b1b1b;
}
*{box-sizing:border-box;margin:0;padding:0}
html,body{width:1200px;height:2794px;overflow:hidden}
body{position:relative;background:var(--white);font-family:"Open Sans",sans-serif;color:var(--text)}
.abs{position:absolute}
.hero-photo{left:0;top:0;width:1200px;height:760px;background:radial-gradient(ellipse at 60% 40%,#4a4642 0%,#34312e 55%,#221f1d 100%)}
.brand{display:flex;align-items:center;gap:14px}
.brand-dot{width:52px;height:52px;border-radius:50%;background:var(--red);flex:none}
.brand-name{font-family:"Oswald",sans-serif;font-weight:500;font-size:38px;line-height:1;letter-spacing:1px}
.brand-tag{font-family:"Oswald",sans-serif;font-size:12.5px;letter-spacing:3.2px;text-transform:uppercase;margin-top:6px}
.hero-brand{left:0;width:1200px;top:60px;justify-content:center;color:var(--white)}
.nav{top:180px;left:0;width:1200px;height:40px}
.nav a{position:absolute;font-family:"Oswald",sans-serif;font-weight:500;font-size:23px;color:var(--white);text-decoration:none;text-transform:uppercase}
.hero-title{top:348px;left:0;width:1200px;text-align:center;color:var(--white);font-family:"Oswald",sans-serif;font-weight:500;font-size:38px;line-height:46px;letter-spacing:2px;text-transform:uppercase}
.btn{display:flex;align-items:center;justify-content:center;font-family:"Oswald",sans-serif;font-weight:500;font-size:26px;text-transform:uppercase;border-radius:10px;height:51px}
.btn-outline{left:400px;top:492px;width:205px;background:var(--white);color:var(--red);border:2px solid var(--red)}
.btn-solid{left:621px;top:492px;width:206px;background:var(--red);color:var(--white);border:2px solid var(--white)}
.dot{top:637px;width:16px;height:16px;border-radius:50%;background:#ccc;border:3px solid var(--red)}
.section-title{left:0;width:1200px;text-align:center;font-family:"Oswald",sans-serif;font-weight:600;font-size:40px;text-transform:uppercase;color:var(--ink)}
.about-copy{left:118px;top:950px;width:522px;font-size:17px;line-height:21px;letter-spacing:.55px}
.about-copy p+p{margin-top:21px}
.checklist{list-style:none;width:300px}
.checklist li{display:flex;align-items:center;height:37.5px;font-size:18px;letter-spacing:.3px}
.checklist svg{width:24px;height:24px;margin:0 24px 0 3px;flex:none}
.frame-grey{background:var(--grey)}
.accent-red{background:var(--red)}
.accent-dark{background:#231f20}
.service-label{top:2132px;width:320px;text-align:center;font-weight:600;font-size:21px;text-transform:uppercase;color:var(--ink)}
.footer-brand{left:108px;top:2372px;color:var(--ink)}
.footer-brand .brand-name{font-size:36px}
.contact-info{left:117px;top:2482px;font-size:16px;line-height:33px}
.contact-info strong{font-size:18px;letter-spacing:.5px}
.copyright{left:115px;top:2670px;color:var(--red);font-size:15px}
.touch-title{left:735px;top:2362px;font-family:"Oswald",sans-serif;font-weight:600;font-size:40px;text-transform:uppercase;color:var(--ink)}
.field{left:735px;width:365px;height:68px;border:2px solid #d0d0d0;border-radius:12px;padding-left:24px;display:flex;align-items:center;color:#9a9a9a;font-size:18px}
.submit{left:735px;top:2642px;width:365px;height:66px;background:var(--red);color:var(--white);border-radius:12px;border:2px solid #c9c9c9}
.bottom-bar{left:0;top:2780px;width:1200px;height:14px;background:var(--ink)}
</style>
</head>
<body>

<svg width="0" height="0" style="position:absolute">
  <defs>
    <symbol id="icon-refresh" viewBox="0 0 24 24">
      <path d="M20 9A9 9 0 0 0 4.5 6.5" fill="none" stroke="#111" stroke-width="2.6"/>
      <path d="M2 3v6h6" fill="#111"/>
      <path d="M4 15a9 9 0 0 0 15.5 2.5" fill="none" stroke="#111" stroke-width="2.6"/>
      <path d="M22 21v-6h-6" fill="#111"/>
    </symbol>
  </defs>
</svg>

<header>
  <div class="abs hero-photo" role="img" aria-label="Dimly lit modern bathroom with a freestanding white tub"></div>
  <div class="abs brand hero-brand">
    <span class="brand-dot"></span>
    <div>
      <div class="brand-name">Evenglaze Refinishing</div>
      <div class="brand-tag">Your refinishing and repair experts</div>
    </div>
  </div>
  <nav class="abs nav">
    <a style="left:208px">Home</a>
    <a style="left:330px">About</a>
    <a style="left:462px">Services</a>
    <a style="left:619px">FAQ</a>
    <a style="left:717px">Testimonials</a>
    <a style="left:918px">Contact</a>
  </nav>
  <h1 class="abs hero-title">Evenglaze Refinishing refinish steel,porcelain,<br>cast iron and fibre glass tub to look new.</h1>
  <a class="abs btn btn-outline">Read more</a>
  <a class="abs btn btn-solid">Get a quote</a>
  <span class="abs dot" style="left:573px"></span>
  <span class="abs dot" style="left:602px"></span>
  <span class="abs dot" style="left:631px"></span>
  <svg class="abs" style="left:0;top:660px" width="1200" height="160" viewBox="0 0 1200 160" preserveAspectRatio="none">
    <path d="M0 90V160H1200V80C900 60 400 70 0 130Z" fill="#fff"/>
    <path d="M0 70C400 10 800 0 1200 10V40C800 30 400 45 0 105Z" fill="#111"/>
    <path d="M0 105C400 45 800 30 1200 40V80C800 55 400 70 0 132Z" fill="#ec1c24"/>
    <path d="M0 132C400 70 800 55 1200 80V150C900 80 400 80 0 140Z" fill="#111"/>
    <path d="M0 140C400 80 900 80 1200 150V160H0Z" fill="#fff"/>
  </svg>
</header>

<section>
  <h2 class="abs section-title" style="top:820px">About us</h2>
  <div class="abs about-copy">
    <p>We are experts at repairing and refinishing kitchen and bathroom surfaces to look like new. Commonly referred to as refinishing, reglazing, resurfacing, or painting a tub - Evenglaze Refinishing locations have been providing this service.</p>
    <p>When we refinish your tub, it is done in place which saves you from additional demolition and repair expenses involved with typical remodeling.</p>
  </div>
  <ul class="abs checklist" style="left:119px;top:1164px">
    <li><svg><use href="#icon-refresh"/></svg>Bathtubs</li>
    <li><svg><use href="#icon-refresh"/></svg>Showers</li>
    <li><svg><use href="#icon-refresh"/></svg>Sinks</li>
    <li><svg><use href="#icon-refresh"/></svg>Countertops</li>
    <li><svg><use href="#icon-refresh"/></svg>Splash boards</li>
  </ul>
  <ul class="abs checklist" style="left:399px;top:1164px">
    <li><svg><use href="#icon-refresh"/></svg>Porcelain</li>
    <li><svg><use href="#icon-refresh"/></svg>Enameled Cast Iron</li>
    <li><svg><use href="#icon-refresh"/></svg>Tile</li>
    <li><svg><use href="#icon-refresh"/></svg>Fiberglass / Acrylic</li>
    <li><svg><use href="#icon-refresh"/></svg>Cultured marble</li>
  </ul>
  <div class="abs frame-grey" style="left:645px;top:952px;width:300px;height:223px"></div>
  <div class="abs accent-red" style="left:998px;top:1227px;width:98px;height:73px"></div>
  <div class="abs" style="left:670px;top:977px;width:406px;height:300px;background:linear-gradient(160deg,#f2f2f2 0%,#d9dcde 50%,#9a9896 100%)" role="img" aria-label="Bright white kitchen with island and stainless appliances"></div>
  <svg class="abs" style="left:0;top:1400px" width="1200" height="120" viewBox="0 0 1200 120" preserveAspectRatio="none">
    <path d="M0 100C400 20 900 10 1200 25V45C900 30 400 50 0 105Z" fill="#d9d9d9"/>
    <path d="M0 105C400 50 900 30 1200 45V115C900 55 400 62 0 110Z" fill="#111"/>
  </svg>
</section>

<section>
  <h2 class="abs section-title" style="top:1520px;left:-15px">Our services</h2>

  <div class="abs frame-grey" style="left:127px;top:1640px;width:235px;height:235px"></div>
  <div class="abs accent-red" style="left:331px;top:2022px;width:86px;height:64px"></div>
  <div class="abs" style="left:148px;top:1663px;width:250px;height:403px;background:linear-gradient(170deg,#e9e9eb 0%,#d8d5d4 45%,#f4f4f4 65%,#4a4a4c 100%)" role="img" aria-label="Refinished white bathtub with tiled wall"></div>
  <div class="abs service-label" style="left:118px">Bathroom refinishing</div>

  <div class="abs frame-grey" style="left:470px;top:1640px;width:235px;height:235px"></div>
  <div class="abs accent-dark" style="left:674px;top:2022px;width:86px;height:64px"></div>
  <div class="abs" style="left:490px;top:1663px;width:247px;height:403px;background:linear-gradient(170deg,#e4e6e8 0%,#cfb597 50%,#ebe9e6 75%,#b89c7c 100%)" role="img" aria-label="Kitchen with light wood cabinets and white countertop"></div>
  <div class="abs service-label" style="left:457px">Kitchen refinishing</div>

  <div class="abs frame-grey" style="left:808px;top:1640px;width:234px;height:235px"></div>
  <div class="abs accent-red" style="left:1010px;top:2022px;width:87px;height:64px"></div>
  <div class="abs" style="left:829px;top:1663px;width:247px;height:403px;background:linear-gradient(160deg,#c99d55 0%,#efe6d6 40%,#b08a5a 60%,#f2f2f2 75%,#cfcfcf 100%)" role="img" aria-label="Kitchen remodel shown half finished and half as a sketch"></div>
  <div class="abs service-label" style="left:801px">Remodeling</div>
</section>

<footer>
  <svg class="abs" style="left:0;top:2240px" width="1200" height="120" viewBox="0 0 1200 120" preserveAspectRatio="none">
    <path d="M0 90C400 20 900 10 1200 30V55C900 30 400 50 0 95Z" fill="#ec1c24"/>
    <path d="M0 95C400 50 900 30 1200 55V115C900 58 400 70 0 100Z" fill="#111"/>
  </svg>
  <div class="abs brand footer-brand">
    <span class="brand-dot"></span>
    <div>
      <div class="brand-name">Evenglaze Refinishing</div>
      <div class="brand-tag">Your refinishing and repair experts</div>
    </div>
  </div>
  <div class="abs contact-info">
    <strong>Suite # 412, 38th Avenue, NYC</strong><br>
    USA | Brookvale, New York<br>
    E-mail: contact@evenglazesite.com<br>
    Tel: +1 (555) 204-7831
  </div>
  <div class="abs copyright">Copyright 2023 Evenglaze Refinishing. All rights</div>

  <h2 class="abs touch-title">Get in touch</h2>
  <div class="abs field" style="top:2457px">Full Name</div>
  <div class="abs field" style="top:2546px">Phone #</div>
  <a class="abs btn submit">Submit now</a>
  <div class="abs bottom-bar"></div>
</footer>

</body>
</html>
```